Grafik für Software-Entwicklungsunternehmen gesucht
Zielgruppe
Moorstep ist ein Software-Entwicklungsunternehmen, welches die Applikation PLAN7Site für Ihre Kunden betreibt und weiter entwickelt. Die Software arbeitet mit KI und augmendet reality uns ist technologisch führend. Alle weiteren Informationen in der PPT.
Aufgabenstellung
Wir brauchen in der Powerpoint-Präsentation eine super coole Grafik, welche die Hauptfunktionalitäten respektive der Prozess zeigt. Die Grafik muss in 3 Prozess-Schritten animiert werden können. Die Datei 'Prozessgrafik' muss als Grafik erstellt werden. Sollte das Budget für animierte Darstellung nicht ausreichen dann bitte melde. Evtl. führen wir den Auftrag dann weiter (Webseite/Kundenpräsentation)

```html
<!DOCTYPE html>
<html lang="de">
<head>
<meta charset="utf-8">
<title>Prozess – PLAN7Site</title>
<link href="https://fonts.googleapis.com/css2?family=Arimo:wght@400;700&display=swap" rel="stylesheet">
<style>
  :root {
    --ink: #111111;
    --teal-light: #12c4c4;
    --teal-mid: #0aa8a8;
    --teal-dark: #0e7f7f;
    --heading-mid: #12b0b4;
    --text: #1c2a30;
    --white: #ffffff;
    --bg-soft: #eef6f9;
    --bg-blue: #9fd6ea;
  }
  html, body {
    margin: 0;
    padding: 0;
    overflow: hidden;
    background: var(--white);
  }
  .slide {
    position: relative;
    width: 1200px;
    height: 675px;
    overflow: hidden;
    font-family: "Arimo", Arial, sans-serif;
    background: var(--white);
  }
  .backdrop {
    position: absolute;
    inset: 0;
    background:
      radial-gradient(ellipse 420px 520px at 1060px 330px, rgba(80,180,220,0.45), rgba(80,180,220,0) 70%),
      radial-gradient(ellipse 700px 160px at 520px 610px, rgba(90,200,225,0.45), rgba(90,200,225,0) 75%),
      radial-gradient(ellipse 300px 120px at 250px 330px, rgba(150,215,235,0.35), rgba(150,215,235,0) 75%),
      linear-gradient(100deg, #ffffff 0%, var(--bg-soft) 45%, #d7eef6 100%);
  }
  .slide-title {
    position: absolute;
    left: 51px;
    top: 46px;
    margin: 0;
    font-size: 38px;
    font-weight: 400;
    color: var(--ink);
  }
  .diagram {
    position: absolute;
    inset: 0;
  }
  .step-heading { font-weight: 700; font-size: 28px; }
  .step-heading.planning { fill: var(--teal-light); }
  .step-heading.execution { fill: var(--heading-mid); }
  .step-heading.lifecycle { fill: var(--teal-dark); }
  .step-list { font-size: 12.5px; fill: var(--text); }
  .product-label { font-weight: 700; font-size: 24px; fill: var(--white); }
  .icon-line { fill: none; stroke: var(--teal-light); stroke-width: 1.6; stroke-linecap: round; stroke-linejoin: round; }
</style>
</head>
<body>
<div class="slide">
  <div class="backdrop" role="img" aria-label="Abstraktes türkisfarbenes Netzwerk-Geflecht als Hintergrundbild"></div>

  <h1 class="slide-title">Prozess</h1>

  <svg class="diagram" width="1200" height="675" viewBox="0 0 1200 675" xmlns="http://www.w3.org/2000/svg">
    <defs>
      <linearGradient id="panel-left" x1="0" x2="1" y1="0" y2="0">
        <stop offset="0" stop-color="#ffffff" stop-opacity="0"/>
        <stop offset="0.25" stop-color="#ffffff" stop-opacity="0.7"/>
        <stop offset="1" stop-color="#ffffff" stop-opacity="0.9"/>
      </linearGradient>
      <linearGradient id="panel-right" x1="0" x2="1" y1="0" y2="0">
        <stop offset="0" stop-color="#ffffff" stop-opacity="0.92"/>
        <stop offset="0.7" stop-color="#ffffff" stop-opacity="0.6"/>
        <stop offset="1" stop-color="#ffffff" stop-opacity="0"/>
      </linearGradient>
    </defs>

    <!-- Step 1: Planung -->
    <g class="step step-planning">
      <polygon points="356,322 409,225 522,225 575,322 522,420 409,420" fill="var(--teal-light)"/>
      <polygon points="156,257 503,257 539,322 503,388 156,388" fill="url(#panel-left)"/>
      <text class="step-heading planning" x="174" y="297">1.PLANUNG</text>
      <text class="step-list" x="174" y="324">I. Projekterfassung und Milestones</text>
      <text class="step-list" x="174" y="339">II. Schnittstellen-Management</text>
      <text class="step-list" x="174" y="354">III. BIM-Viewer</text>
      <g class="icon-monitor">
        <rect class="icon-line" x="432" y="300" width="62" height="41" rx="3"/>
        <line class="icon-line" x1="432" y1="335" x2="494" y2="335"/>
        <line class="icon-line" x1="463" y1="341" x2="463" y2="348"/>
        <line class="icon-line" x1="452" y1="349" x2="474" y2="349"/>
        <polyline class="icon-line" points="449,309 451,311 455,307"/>
        <polyline class="icon-line" points="449,317 451,319 455,315"/>
        <polyline class="icon-line" points="449,325 451,327 455,323"/>
        <line class="icon-line" x1="460" y1="309" x2="477" y2="309"/>
        <line class="icon-line" x1="460" y1="317" x2="477" y2="317"/>
        <line class="icon-line" x1="460" y1="325" x2="477" y2="325"/>
      </g>
    </g>

    <!-- Step 2: Ausführung -->
    <g class="step step-execution">
      <polygon points="524,223 578,126 694,126 747,223 694,322 578,322" fill="var(--teal-mid)"/>
      <polygon points="561,223 598,159 938,159 938,289 598,289" fill="url(#panel-right)"/>
      <rect x="598" y="197" width="69" height="44" rx="6" fill="var(--teal-light)" opacity="0.22" role="img" aria-label="Piktogramm: Person mit Puzzleteilen"/>
      <text class="step-heading execution" x="698" y="197">2.AUSFÜHRUNG</text>
      <text class="step-list" x="701" y="217">I. Intelligentes Baumanagement</text>
      <text class="step-list" x="701" y="232">II. Augmented reality</text>
      <text class="step-list" x="701" y="247">III. Künstlichen Intelligenz bei…</text>
      <text class="product-label" x="580" y="313">PLAN7Site</text>
    </g>

    <!-- Step 3: Lifecycle-Management -->
    <g class="step step-lifecycle">
      <polygon points="524,422 578,324 694,324 747,422 694,520 578,520" fill="var(--teal-dark)"/>
      <polygon points="561,422 598,357 1062,357 1062,487 598,487" fill="url(#panel-right)"/>
      <rect x="600" y="403" width="53" height="44" rx="6" fill="var(--teal-dark)" opacity="0.2" role="img" aria-label="Piktogramm: Person mit Pfeilen in alle Richtungen"/>
      <text class="step-heading lifecycle" x="661" y="396">3.LIFECYCLE-MANAGEMENT</text>
      <text class="step-list" x="662" y="414">I. Facility-Management</text>
      <text class="step-list" x="662" y="429">II. Objekt-Abnahme</text>
      <text class="step-list" x="662" y="444">III. Garantieleistungen</text>
      <text class="step-list" x="662" y="459">IV. Mängelbehebung</text>
      <text class="step-list" x="662" y="474">V. «Digitalisierung» Projekt-Owner</text>
    </g>
  </svg>
</div>
</body>
</html>
```